Hoist Ridge Rigging Sales Flyer

I need a professional modern flyer offering our crane services with our phone number and website. The flyer should focus on the blue crane and the red crane (JointArms) but include a small picture of the other cranes as well to show variety. This flyer will be mailed and emailed to a variety of roofing companies, HVAC, pool and mechanical contractors as well as precast concrete companies to attempt to earn their business. 8.5x11 single sided

HoistRidgeRigs.com
555 418-2973 should be number on flyer

```html
<!DOCTYPE html>
<html lang="en">
<head>
<meta charset="utf-8">
<title>Hoist Ridge Rigging – Crane Service Flyer</title>
<link rel="stylesheet" href="https://fonts.googleapis.com/css2?family=Montserrat:wght@800;900&family=Barlow+Condensed:wght@400;500&family=Oswald:wght@500;600&family=Roboto+Slab:wght@400&display=swap">
<style>
:root{
  --ink:#141414;
  --black-band:#161616;
  --red:#d5173a;
  --blue:#3d5fd8;
  --navy:#0d3590;
  --green:#3ec24a;
  --bright-green:#4ee25b;
  --panel-grey:#e4e5e8;
  --stage:#d9d9db;
  --white:#ffffff;
}
*{margin:0;padding:0;box-sizing:border-box}
html,body{width:1200px;height:2163px;overflow:hidden;background:var(--stage)}
.flyer{
  position:absolute;left:30px;top:346px;width:988px;height:1275px;
  transform:scale(1.1538);transform-origin:0 0;
  background:var(--white);overflow:hidden;
  box-shadow:0 6px 18px rgba(0,0,0,.25);
}
.backdrop{position:absolute;inset:0}
.photo{position:absolute;border-radius:18px}
.photo-blue-boom{left:300px;top:22px;width:170px;height:330px;background:linear-gradient(180deg,#2b3f9a,#4a5cb0)}
.photo-blue-truck{left:140px;top:372px;width:420px;height:196px;background:linear-gradient(90deg,#2f3f8e 0%,#5d6598 45%,#e8e9ee 75%,#b9bbc2 100%)}
.photo-yellow{left:330px;top:636px;width:140px;height:112px;background:linear-gradient(135deg,#f2d21a,#d4ad14 60%,#6a6a6a)}
.photo-red-boom{left:478px;top:572px;width:150px;height:430px;background:linear-gradient(180deg,#8d8f96 0%,#e2613e 35%,#c94a2f 100%)}
.photo-red-truck{left:430px;top:1020px;width:330px;height:150px;background:linear-gradient(180deg,#6b5656,#3a3a3e 60%,#2a2a2d)}
.photo-icon{left:805px;top:520px;width:90px;height:100px;background:linear-gradient(180deg,var(--red),#2a2a2a)}
.photo-lattice{left:815px;top:1045px;width:140px;height:200px;background:linear-gradient(180deg,#dcdce0,#77777c)}
.headline{
  position:absolute;right:85px;top:40px;text-align:right;
  font-family:"Montserrat",sans-serif;font-weight:900;line-height:.9;letter-spacing:-1px;
}
.headline .crane{display:block;font-size:104px;color:var(--red)}
.headline .service{display:block;font-size:62px;color:var(--blue);margin-top:6px}
.headline .done{display:block;font-size:92px;color:var(--bright-green);margin-top:4px}
.headline .done small{font-size:58px}
.headline .promised{display:block;font-size:68px;color:var(--blue);margin-top:6px}
.headline-rule{position:absolute;left:933px;top:55px;width:3px;height:275px;background:var(--green)}
.tagline{
  position:absolute;right:53px;top:352px;text-align:right;color:var(--white);
  font-family:"Barlow Condensed",sans-serif;font-size:21px;line-height:26px;
}
.brand{
  position:absolute;left:40px;top:300px;width:250px;
  font-family:"Oswald",sans-serif;font-weight:600;font-size:32px;line-height:1.05;color:var(--ink);
  display:flex;align-items:center;gap:10px;
}
.brand .dot{width:18px;height:18px;background:var(--red);flex:none}
.services-title{
  position:absolute;left:0;top:628px;width:302px;height:60px;
  background:var(--red);border-radius:0 30px 30px 0;
  color:var(--white);font-family:"Oswald",sans-serif;font-weight:600;font-size:40px;
  line-height:60px;padding-left:46px;letter-spacing:.5px;
}
.services{position:absolute;left:46px;top:705px;list-style:none}
.services li{
  display:flex;align-items:center;gap:14px;height:57px;width:330px;white-space:nowrap;
  font-family:"Oswald",sans-serif;font-weight:600;font-size:26px;color:var(--ink);
  border-bottom:1px dotted #b9b9bd;
}
.services li:last-child{border-bottom:none}
.services svg{width:26px;height:26px;flex:none}
.trusted{
  position:absolute;right:47px;top:732px;width:300px;text-align:right;
  font-family:"Barlow Condensed",sans-serif;font-size:18px;line-height:22px;color:var(--ink);
}
.trusted h2{font-weight:500;font-size:22px;color:var(--green);margin-bottom:2px}
.perks{position:absolute;left:735px;top:880px;display:flex}
.perk{width:120px;text-align:center;font-family:"Oswald",sans-serif;font-weight:500;font-size:20px;line-height:22px;color:var(--ink)}
.perk svg{width:76px;height:76px;display:block;margin:0 auto 4px}
.perk-divider{width:1px;height:120px;background:#888;margin-top:2px}
.footer-text{position:absolute;color:var(--white)}
.phone{left:48px;top:1190px;font-family:"Oswald",sans-serif;font-weight:500;font-size:34px;display:flex;align-items:center;gap:8px}
.phone svg{width:22px;height:30px}
.web{left:48px;top:1237px;font-family:"Roboto Slab",serif;font-size:22px;display:flex;align-items:center;gap:6px}
.web svg{width:11px;height:11px}
.addresses{left:468px;top:1190px;font-family:"Roboto Slab",serif;font-size:14px;line-height:19px}
.addresses .state{display:flex;align-items:center;gap:4px;margin-left:-14px}
.addresses svg{width:10px;height:12px}
</style>
</head>
<body>
<main class="flyer">
  <svg class="backdrop" viewBox="0 0 988 1275" preserveAspectRatio="none" aria-hidden="true">
    <rect width="988" height="480" fill="var(--black-band)"/>
    <polygon points="0,40 300,40 560,260 560,480 988,480 988,610 0,610" fill="var(--white)"/>
    <polygon points="0,565 55,610 560,610 700,1175 0,1175" fill="var(--panel-grey)"/>
    <polygon points="0,1175 340,1175 405,1275 0,1275" fill="var(--red)"/>
    <polygon points="340,1175 725,1175 795,1275 405,1275" fill="var(--navy)"/>
    <polygon points="725,1175 988,1175 988,1275 795,1275" fill="var(--green)"/>
  </svg>

  <div class="photo photo-blue-boom" role="img" aria-label="Blue knuckle-boom crane arm raised high"></div>
  <div class="photo photo-blue-truck" role="img" aria-label="White truck carrying the blue crane with outriggers"></div>
  <div class="photo photo-yellow" role="img" aria-label="Yellow mobile crane"></div>
  <div class="photo photo-red-boom" role="img" aria-label="Red knuckle-boom crane arm extended"></div>
  <div class="photo photo-red-truck" role="img" aria-label="Dark truck loaded with materials carrying the red crane"></div>
  <div class="photo photo-icon" role="img" aria-label="Small red crane truck icon"></div>
  <div class="photo photo-lattice" role="img" aria-label="White lattice crawler crane"></div>

  <div class="brand"><span class="dot"></span><span>Hoist Ridge Rigging</span></div>

  <h1 class="headline">
    <span class="crane">CRANE</span>
    <span class="service">SERVICE</span>
    <span class="done">DONE <small>AS</small></span>
    <span class="promised">PROMISED</span>
  </h1>
  <div class="headline-rule"></div>
  <p class="tagline">Crane Service Partners That Meet Deadlines,<br>Prioritize Safety, And Stay Within Budget<br>With End-to-end Support.</p>

  <div class="services-title">OUR SERVICES</div>
  <ul class="services">
    <li><svg viewBox="0 0 26 26"><circle cx="13" cy="13" r="11" fill="none" stroke="var(--ink)" stroke-width="1.6"/><path d="M8 13l4 4 9-10" fill="none" stroke="var(--red)" stroke-width="2"/></svg>CONTAINER</li>
    <li><svg viewBox="0 0 26 26"><circle cx="13" cy="13" r="11" fill="none" stroke="var(--ink)" stroke-width="1.6"/><path d="M8 13l4 4 9-10" fill="none" stroke="var(--red)" stroke-width="2"/></svg>GENERAL CONSTRUCTION</li>
    <li><svg viewBox="0 0 26 26"><circle cx="13" cy="13" r="11" fill="none" stroke="var(--ink)" stroke-width="1.6"/><path d="M8 13l4 4 9-10" fill="none" stroke="var(--red)" stroke-width="2"/></svg>HEAVY MACHINERY MOVING</li>
    <li><svg viewBox="0 0 26 26"><circle cx="13" cy="13" r="11" fill="none" stroke="var(--ink)" stroke-width="1.6"/><path d="M8 13l4 4 9-10" fill="none" stroke="var(--red)" stroke-width="2"/></svg>HVAC</li>
    <li><svg viewBox="0 0 26 26"><circle cx="13" cy="13" r="11" fill="none" stroke="var(--ink)" stroke-width="1.6"/><path d="M8 13l4 4 9-10" fill="none" stroke="var(--red)" stroke-width="2"/></svg>POWER TRANSFORMER</li>
    <li><svg viewBox="0 0 26 26"><circle cx="13" cy="13" r="11" fill="none" stroke="var(--ink)" stroke-width="1.6"/><path d="M8 13l4 4 9-10" fill="none" stroke="var(--red)" stroke-width="2"/></svg>STEEL CONSTRUCTION</li>
    <li><svg viewBox="0 0 26 26"><circle cx="13" cy="13" r="11" fill="none" stroke="var(--ink)" stroke-width="1.6"/><path d="M8 13l4 4 9-10" fill="none" stroke="var(--red)" stroke-width="2"/></svg>TREE REMOVAL</li>
  </ul>

  <div class="trusted">
    <h2>Trusted Crane Company In OH. &amp; IN.</h2>
    <p>Our team of project planners and operators is committed to serving your project's needs everystep of the way, ensuring safety and done right the first time without major disruptions.</p>
  </div>

  <div class="perks">
    <div class="perk">
      <svg viewBox="0 0 76 76"><circle cx="38" cy="38" r="36" fill="var(--green)"/><circle cx="38" cy="38" r="28" fill="none" stroke="var(--white)" stroke-width="3"/><circle cx="38" cy="42" r="17" fill="var(--white)"/><rect x="34" y="16" width="8" height="6" fill="var(--white)"/><rect x="36.5" y="31" width="3" height="12" fill="var(--green)"/></svg>
      Fastest<br>Workflow
    </div>
    <div class="perk-divider"></div>
    <div class="perk">
      <svg viewBox="0 0 76 76"><circle cx="38" cy="38" r="36" fill="var(--green)"/><circle cx="38" cy="38" r="28" fill="none" stroke="var(--white)" stroke-width="3"/><path d="M32 20h12l-4 7c10 4 13 12 13 18 0 8-7 11-15 11s-15-3-15-11c0-6 3-14 13-18z" fill="var(--white)"/><text x="38" y="50" text-anchor="middle" font-family="Oswald,sans-serif" font-size="16" font-weight="600" fill="var(--green)">$</text></svg>
      Budget<br>Friendly
    </div>
  </div>

  <div class="footer-text phone">
    <svg viewBox="0 0 22 30"><rect x="4" y="2" width="14" height="26" rx="3" fill="none" stroke="var(--white)" stroke-width="2"/><line x1="9" y1="24" x2="13" y2="24" stroke="var(--white)" stroke-width="2"/></svg>
    (555) 418-2973
  </div>
  <div class="footer-text web">
    <svg viewBox="0 0 12 12"><circle cx="6" cy="6" r="5" fill="none" stroke="var(--white)" stroke-width="1.4"/><line x1="1" y1="6" x2="11" y2="6" stroke="var(--white)"/></svg>
    HoistRidgeRigs.com
  </div>
  <div class="footer-text addresses">
    <div class="state"><svg viewBox="0 0 10 12"><path d="M5 11C2 7 1 5.5 1 4a4 4 0 018 0c0 1.5-1 3-4 7z" fill="none" stroke="var(--white)"/></svg>Ohio</div>
    <div>1820 Harbor Ave, Akron, OH 44310</div>
    <div class="state"><svg viewBox="0 0 10 12"><path d="M5 11C2 7 1 5.5 1 4a4 4 0 018 0c0 1.5-1 3-4 7z" fill="none" stroke="var(--white)"/></svg>Indiana</div>
    <div>9050 Creek Rd, Noblesville, IN 46060</div>
  </div>
</main>
</body>
</html>
```